Billboard design - consider what a billboard is

Design a billboard using my logo - Billboard is 6m x 3m
A Billboard is advertising for my company that is on a big sign.

Has to be clean and easy to read, and ideally highlights that we are Residential and Commercial builders.

Keep it clean and easy to read

The contact number for the board is

022 583 7092
www.harbourframeworks.co.nz
info@harbourframeworks.co.nz

Doesnt have to have all contact details if it doesnt fit

Has to catch peoples attention to contact us if they need a builder

Can you please change the sign to be all white writing, with black background ?
Updates

Please consider what a billboard is...

The design needs to be suitable for a billboard..

Target Market(s)

people driving past

Industry/Entity Type

Construction

Logo Text

Wellington Builder, website email address, contact number

Colors
0054AA
0677BA
7BADD7
CADEEF
E8F1F8

Requirements
Must have
• Easy to read
Nice to have
• easy to read, can clearly see contact details

```html
<!DOCTYPE html>
<html lang="en">
<head>
<meta charset="utf-8">
<title>Harbour Frameworks Billboard</title>
<link href="https://fonts.googleapis.com/css2?family=Archivo+Black&family=Montserrat:wght@500&family=Open+Sans:wght@600;700&display=swap" rel="stylesheet">
<style>
  :root {
    --page: #ffffff;
    --board: #000000;
    --tab-edge: #1f2a6b;
    --tab-fill: #5585c8;
    --bar-top: #3a4c98;
    --bar-bottom: #5b82c2;
    --url-ink: #1b3670;
    --star: #19b3ea;
    --sky-top: #4f80c4;
    --sky-mid: #6f9ed4;
    --sky-low: #8fb3dc;
    --band: #1a3f7a;
    --brand: #4f82c9;
    --white: #ffffff;
    --shadow: #1d3570;
  }
  html, body {
    margin: 0;
    width: 1200px;
    height: 1200px;
    overflow: hidden;
    background: var(--page);
  }
  .canvas { position: relative; width: 1200px; height: 1200px; }
  .billboard {
    position: absolute;
    left: 102px; top: 353px;
    width: 1004px; height: 502px;
    background: var(--board);
    overflow: hidden;
  }
  .tab {
    position: absolute;
    left: 24px; top: 10px;
    width: 323px; height: 57px;
    background: var(--tab-edge);
    border-radius: 6px 6px 0 0;
  }
  .tab-inner {
    position: absolute;
    left: 4px; top: 4px; right: 4px; bottom: 0;
    background: var(--tab-fill);
    border-radius: 4px 4px 0 0;
    display: flex; align-items: center;
  }
  .tab-icon {
    width: 34px; height: 34px; margin-left: 7px;
    background: var(--white); border-radius: 4px;
  }
  .tab-title {
    margin-left: 8px;
    font: 500 18px "Montserrat", sans-serif;
    letter-spacing: 0.5px;
    color: var(--white);
  }
  .toolbar {
    position: absolute;
    left: 0; top: 67px; width: 100%; height: 58px;
    background: linear-gradient(180deg, var(--bar-top), var(--bar-bottom));
  }
  .nav-icons { position: absolute; left: 12px; top: 15px; }
  .address {
    position: absolute;
    left: 143px; top: 7px;
    width: 764px; height: 45px;
    background: var(--white);
    display: flex; align-items: center;
  }
  .address .lock { margin-left: 11px; }
  .address .url {
    margin-left: 14px;
    font: 400 39px "Open Sans", sans-serif;
    color: var(--url-ink);
    line-height: 1;
    letter-spacing: 0.5px;
  }
  .address .star { position: absolute; right: 12px; top: 8px; }
  .brand-panel {
    position: absolute;
    left: 0; top: 125px; width: 383px; height: 377px;
  }
  .brand-name {
    position: absolute;
    left: 40px; top: 118px;
    display: flex; align-items: center; gap: 14px;
  }
  .brand-mark { width: 34px; height: 34px; background: var(--brand); }
  .brand-word {
    font: 700 40px/1.05 "Open Sans", sans-serif;
    color: var(--brand);
  }
  .services {
    position: absolute;
    left: 10px; bottom: 8px;
    font: 500 15.5px "Montserrat", sans-serif;
    color: var(--white);
    letter-spacing: 0.6px;
    white-space: nowrap;
  }
  .hero {
    position: absolute;
    left: 383px; top: 125px; width: 621px; height: 377px;
    background: linear-gradient(180deg, var(--sky-top) 0%, var(--sky-mid) 55%, var(--sky-low) 100%);
  }
  .headline {
    position: absolute;
    left: 0; right: 0; top: 66px;
    text-align: center;
    font: 400 44px/60px "Archivo Black", sans-serif;
    color: var(--white);
    text-shadow: 3px 3px 0 var(--shadow);
    margin: 0;
    padding-left: 48px;
  }
  .phone-band { position: absolute; left: 0; bottom: 0; }
  .phone {
    position: absolute;
    left: 80px; right: 0; bottom: 14px;
    text-align: center;
    font: 600 74px "Open Sans", sans-serif;
    color: var(--white);
    letter-spacing: 1px;
  }
</style>
</head>
<body>
<div class="canvas">
  <div class="billboard">
    <div class="tab">
      <div class="tab-inner">
        <div class="tab-icon"></div>
        <span class="tab-title">Homes.Offices.Excellence</span>
      </div>
    </div>

    <div class="toolbar">
      <svg class="nav-icons" width="120" height="30" viewBox="0 0 120 30" fill="none" stroke="#ffffff" stroke-width="1.8" stroke-linecap="round" stroke-linejoin="round">
        <path d="M3 14 H22 M3 14 L9 8 M3 14 L9 20"/>
        <path d="M40 14 H59 M59 14 L53 8 M59 14 L53 20"/>
        <path d="M105 7 A9 9 0 1 0 111 12"/>
        <path d="M106 4 L111 6 L108 10"/>
      </svg>
      <div class="address">
        <svg class="lock" width="22" height="28" viewBox="0 0 22 28" fill="none" stroke="#1b3670" stroke-width="2">
          <rect x="2" y="12" width="18" height="14" rx="2"/>
          <path d="M6 12 V8 A5 5 0 0 1 16 8 V12"/>
        </svg>
        <span class="url">harbourframeworks.com</span>
        <svg class="star" width="30" height="30" viewBox="0 0 24 24">
          <path fill="#19b3ea" d="M12 1.5 L15 9 L23 9.3 L16.8 14.3 L19 22 L12 17.6 L5 22 L7.2 14.3 L1 9.3 L9 9 Z"/>
        </svg>
      </div>
    </div>

    <div class="brand-panel">
      <div class="brand-name">
        <div class="brand-mark"></div>
        <div class="brand-word">Harbour<br>Frameworks</div>
      </div>
      <div class="services">CONSTRUCTION | MAINTENENCE | FITOUTS</div>
    </div>

    <div class="hero" role="img" aria-label="Photo of tower cranes and street lights against a blue sky at a construction site">
      <h1 class="headline">Raising Structures<br>Realizing Dreams</h1>
      <svg class="phone-band" width="621" height="107" viewBox="0 0 621 107">
        <path fill="#1a3f7a" d="M86 0 H621 V107 H0 L62 12 Q70 0 86 0 Z"/>
      </svg>
      <div class="phone">022 583 7092</div>
    </div>
  </div>
</div>
</body>
</html>
```